Business Card Design

We need a Business card design for our Family Dental Clinic.
Colour choices - White, blue and golden to go with the logo.
Industry/Entity Type
Business
Contact Information for Business Card
Side 1
DR MONA PELLINGHAM
BDS
Suite 6, Level 2, 418 Wexbridge Street
Fernvale North, VIC 3058
Fax : 9476 2035
Email: info@fernvaledentalgroup.com.au
Website: fernvaledentalgroup.com.au
Phone(image) - 9476 2035 (bigger size)
Please make sure that you produce 3 files with the same design
1) As per above
2) With out the Name ( i. e DR Mona Pellingham BDS)
3) Just the card template (no texts)
Side 2
......................................... at ........................
Please give 24 hours notice if you cannot keep this appointment

```html
<!DOCTYPE html>
<html lang="en">
<head>
<meta charset="utf-8">
<title>Fernvale Dental Group – Business Card</title>
<link rel="stylesheet" href="https://fonts.googleapis.com/css2?family=Open+Sans:wght@400;600;700&display=swap">
<style>
  :root{
    --bg:#e9e6e1;
    --card:#ffffff;
    --card-shade:#e3e4e8;
    --blue:#1e46d8;
    --blue-light:#3f78f0;
    --blue-deep:#0f2fb0;
    --gold:#f0a21c;
    --ink:#3c3c3c;
    --muted:#6a6a6a;
  }
  *{margin:0;padding:0;box-sizing:border-box}
  html,body{width:1200px;height:894px;overflow:hidden}
  body{background:var(--bg);font-family:"Open Sans",Arial,sans-serif;position:relative}

  .card{
    position:absolute;border-radius:22px;overflow:hidden;
    background:linear-gradient(160deg,var(--card) 40%,var(--card-shade) 100%);
    box-shadow:0 10px 26px rgba(0,0,0,.22);
  }
  .card--front{left:100px;top:270px;width:620px;height:354px}
  .card--back{left:790px;top:137px;width:354px;height:620px}

  /* brand */
  .brand{display:flex;align-items:center;position:absolute}
  .brand__dot{border-radius:50%;background:var(--gold);flex:none}
  .brand__name{color:var(--blue);font-weight:600;letter-spacing:1px;text-transform:uppercase;line-height:1.15}
  .card--front .brand{left:0;right:0;top:92px;justify-content:center;gap:18px}
  .card--front .brand__dot{width:60px;height:60px}
  .card--front .brand__name{font-size:30px}

  .card--back .brand{right:30px;top:38px;gap:12px}
  .card--back .brand__dot{width:40px;height:40px}
  .card--back .brand__name{font-size:17px}

  /* appointment reminder */
  .appointment{position:absolute;left:60px;right:60px;top:220px;text-align:center;color:var(--ink)}
  .appointment__slot{display:flex;align-items:flex-end;gap:12px;font-size:16px}
  .appointment__line{flex:1;border-bottom:2px dotted var(--muted);height:18px}
  .appointment__line--short{flex:0 0 150px}
  .appointment__note{margin-top:22px;font-size:14px;color:var(--muted)}

  /* back side */
  .side-band{
    position:absolute;left:0;top:0;bottom:0;width:26px;
    background:linear-gradient(180deg,var(--blue-deep),var(--blue-light) 50%,var(--blue-deep));
  }
  .name-tag{
    position:absolute;right:0;top:128px;width:306px;height:84px;
    background:linear-gradient(180deg,var(--blue-light),var(--blue-deep));
    border-radius:26px 0 0 26px;color:#fff;padding:15px 0 0 28px;
  }
  .name-tag__name{font-size:20px;font-weight:700;letter-spacing:.5px}
  .name-tag__role{font-size:14px;letter-spacing:1px;margin-top:2px}

  .contacts{position:absolute;left:50px;right:18px;top:250px;list-style:none}
  .contacts li{display:flex;align-items:flex-start;gap:10px;margin-bottom:16px;
    font-size:13px;line-height:18px;color:var(--ink)}
  .contacts svg{width:18px;height:18px;flex:none}
  .contacts .contacts__phone{font-size:20px;line-height:24px;font-weight:700;color:var(--blue)}
  .contacts .contacts__phone svg{width:24px;height:24px}
  .contacts__label{color:var(--muted)}
</style>
</head>
<body>

<section class="card card--front">
  <div class="brand">
    <span class="brand__dot"></span>
    <span class="brand__name">Fernvale Dental Group</span>
  </div>

  <div class="appointment">
    <div class="appointment__slot">
      <span class="appointment__line"></span>
      <span>at</span>
      <span class="appointment__line appointment__line--short"></span>
    </div>
    <p class="appointment__note">Please give 24 hours notice if you cannot keep this appointment</p>
  </div>
</section>

<section class="card card--back">
  <div class="side-band"></div>

  <div class="brand">
    <span class="brand__dot"></span>
    <span class="brand__name">Fernvale<br>Dental Group</span>
  </div>

  <div class="name-tag">
    <div class="name-tag__name">DR MONA PELLINGHAM</div>
    <div class="name-tag__role">BDS</div>
  </div>

  <ul class="contacts">
    <li class="contacts__phone">
      <svg viewBox="0 0 20 20"><circle cx="10" cy="10" r="9" fill="none" stroke="var(--gold)" stroke-width="1.6"/><path d="M7 5.5l2 2-1 1.3a6 6 0 0 0 3.2 3.2l1.3-1 2 2-1.3 1.5C9.5 14.2 5.8 10.5 5.5 6.8z" fill="var(--gold)"/></svg>
      9476 2035
    </li>
    <li>
      <svg viewBox="0 0 20 20"><circle cx="10" cy="10" r="9" fill="none" stroke="var(--gold)" stroke-width="1.6"/><rect x="5.5" y="8" width="9" height="6" rx="1" fill="var(--gold)"/><rect x="7" y="5" width="6" height="3.5" fill="none" stroke="var(--gold)" stroke-width="1.2"/></svg>
      <span><span class="contacts__label">Fax:</span> 9476 2035</span>
    </li>
    <li>
      <svg viewBox="0 0 20 20"><circle cx="10" cy="10" r="9" fill="none" stroke="var(--gold)" stroke-width="1.6"/><rect x="5" y="6.5" width="10" height="7" fill="var(--gold)"/><path d="M5 6.5l5 4 5-4" fill="none" stroke="#fff" stroke-width="1"/></svg>
      info@fernvaledentalgroup.com.au
    </li>
    <li>
      <svg viewBox="0 0 20 20"><circle cx="10" cy="10" r="9" fill="none" stroke="var(--gold)" stroke-width="1.6"/><circle cx="10" cy="10" r="5" fill="none" stroke="var(--gold)" stroke-width="1.3"/><path d="M5 10h10M10 5v10" stroke="var(--gold)" stroke-width="1.1"/></svg>
      fernvaledentalgroup.com.au
    </li>
    <li>
      <svg viewBox="0 0 20 20"><circle cx="10" cy="10" r="9" fill="none" stroke="var(--gold)" stroke-width="1.6"/><path d="M10 15s-4-4-4-6.5a4 4 0 0 1 8 0C14 11 10 15 10 15z" fill="var(--gold)"/><circle cx="10" cy="8.5" r="1.4" fill="#fff"/></svg>
      <span>Suite 6, Level 2, 418 Wexbridge Street<br>Fernvale North, VIC 3058</span>
    </li>
  </ul>
</section>

</body>
</html>
```